Verdell Chiropractic, achieve your health goals, get better each day one step at a time

A mobile friendly site, fresh look, easy to navigate, has interface with pw/chirply, etc. Blog posts. Uses new logo. Content and address to current site is mirvaton.com. The current site will give you scope of project for content. The logo is not the final but close. Will upload final next week.
Convey the concept that heath is a process, it does not just happen. We take steps to achieve what we want in life including health.

Target Market(s)

30 to 70 year old. Needing health care

Industry/Entity Type

Health Care

Coding

Coded - Design and coding required

Number of Pages Required

5+ page

Font styles to use
Sans Serif

Colors

Designer to choose colors to be used in the design.

Requirements
Must have
• mobile friendly, easy to navigate, PW/Chirply interface, blog, room for current content
Nice to have
• potential for commerce, statistics
Should not have
• Same old look and feel as everything else out there

```html
<!DOCTYPE html>
<html lang="en">
<head>
<meta charset="utf-8">
<title>Verdell Chiropractic</title>
<link rel="stylesheet" href="https://fonts.googleapis.com/css2?family=Josefin+Sans:wght@400;600&family=EB+Garamond:wght@400&display=swap">
<style>
:root{
  --blue:#2a78b6;
  --blue-dark:#2f7db5;
  --green:#c9d897;
  --green-light:#e1ecc2;
  --button:#6c9cb6;
  --nav:#7fb3c4;
  --ink:#4a4a3e;
  --white:#ffffff;
  --wave:#3a86c8;
}
*{margin:0;padding:0;box-sizing:border-box}
html,body{width:1200px;height:2525px;overflow:hidden;background:var(--white)}
body{position:relative;font-family:"EB Garamond",Georgia,serif;color:var(--ink)}
.abs{position:absolute}
.heading{font-family:"Josefin Sans",Arial,sans-serif;color:var(--blue);font-weight:400;line-height:1.2}
.copy{font-size:18px;line-height:1.42}
.photo{position:absolute;box-shadow:0 2px 6px rgba(0,0,0,.25);border:1px solid #e6e6e6}
.btn{position:absolute;width:168px;height:50px;border-radius:9px;background:linear-gradient(#7eabc3,var(--button));
  color:var(--white);font-family:"Josefin Sans",Arial,sans-serif;font-size:20px;display:flex;align-items:center;justify-content:center;
  box-shadow:0 3px 6px rgba(0,0,0,.3)}
.wave{position:absolute;left:0;width:1200px;height:8px}

/* header */
.top-band{left:0;top:0;width:1200px;height:150px}
.logo-box{left:20px;top:17px;width:300px;height:106px;background:var(--white);border:1px solid #bbb;box-shadow:0 2px 5px rgba(0,0,0,.3);
  display:flex;align-items:center;justify-content:center;gap:10px}
.logo-mark{width:18px;height:18px;background:var(--blue)}
.logo-name{font-family:"Josefin Sans",Arial,sans-serif;font-weight:600;font-size:22px;color:var(--blue)}
.nav{left:345px;top:40px;width:813px;height:61px;background:rgba(110,170,190,.55);border-radius:6px;display:flex;align-items:center;justify-content:space-around;padding:0 10px}
.nav a{display:flex;align-items:center;justify-content:center;height:46px;padding:0 20px;min-width:105px;border-radius:12px;
  background:linear-gradient(#8fc2d2,#5f9db6);color:var(--white);font-family:"Josefin Sans",Arial,sans-serif;font-size:20px;text-decoration:none;
  box-shadow:0 2px 4px rgba(0,0,0,.3)}

/* hero */
.hero{left:0;top:0;width:1200px;height:693px;background:linear-gradient(100deg,#fff3df 0%,#f8d69c 35%,#e9a368 60%,#f6c99a 80%,#fbe6cf 100%)}
.hero-title{left:94px;top:196px;font-size:45px}
.hero-sub{left:96px;top:250px;font-family:"Josefin Sans",Arial,sans-serif;font-size:17px;color:#333}
.hero-copy{left:101px;top:292px;width:235px;font-size:19px;line-height:1.47;color:#3b3325}

/* doctor section */
.doctor{left:0;top:697px;width:1200px;height:577px;background:var(--green)}

/* welcome */
.welcome{left:0;top:1278px;width:1200px;height:492px;background:linear-gradient(90deg,#efe6e0 0%,#f6f1ee 35%,#ffffff 60%)}
.label{font-family:"Josefin Sans",Arial,sans-serif;font-size:20px;color:#333}

/* methodology */
.method{left:0;top:1774px;width:1200px;height:464px;background:var(--green-light)}

/* footer */
.footer{left:0;top:2238px;width:1200px;height:287px;background:var(--blue-dark);box-shadow:inset 0 4px 6px rgba(0,0,0,.2)}
.foot-col{position:absolute;top:2258px;width:230px;color:var(--white)}
.foot-col h3{font-family:"Josefin Sans",Arial,sans-serif;font-weight:400;font-size:22px;letter-spacing:.5px;margin-bottom:16px}
.foot-col p{font-size:14px;line-height:1.4}
.foot-col ul{list-style:none;font-family:"Josefin Sans",Arial,sans-serif;font-size:17px;line-height:1.4}
</style>
</head>
<body>

<!-- hero -->
<div class="abs hero" role="img" aria-label="Photo of a woman relaxing on a treatment table while receiving a shoulder massage"></div>
<svg class="abs top-band" viewBox="0 0 1200 150" aria-hidden="true">
  <rect x="0" y="0" width="1200" height="40" fill="#7ecf8a" opacity=".7"/>
  <rect x="0" y="40" width="1200" height="60" fill="#ffffff" opacity=".55"/>
  <rect x="0" y="100" width="1200" height="48" fill="#ffffff" opacity=".75"/>
</svg>
<div class="abs logo-box"><span class="logo-mark"></span><span class="logo-name">Verdell Chiropractic</span></div>
<nav class="abs nav">
  <a>home</a><a>dr halvik</a><a>testimonials</a><a>faq</a><a>resources</a><a>contact</a>
</nav>
<h1 class="abs heading hero-title">Health is a process</h1>
<p class="abs hero-sub">let’s us guide you through these steps</p>
<p class="abs hero-copy">Nullam sodales, metus fringilla pharetra faucibus, elit ipsum bibendum arcu, id blandit mi neque ut dui. In eu pretium nisl. Vestibulum posuere ut ex non pellentesque.<br>Lorem ipsum dolor sit</p>

<svg class="wave" style="top:689px" viewBox="0 0 1200 8" preserveAspectRatio="none" aria-hidden="true">
  <path d="M0 4 Q10 0 20 4 T40 4 T60 4 T80 4 T100 4 T120 4 T140 4 T160 4 T180 4 T200 4 T220 4 T240 4 T260 4 T280 4 T300 4 T320 4 T340 4 T360 4 T380 4 T400 4 T420 4 T440 4 T460 4 T480 4 T500 4 T520 4 T540 4 T560 4 T580 4 T600 4 T620 4 T640 4 T660 4 T680 4 T700 4 T720 4 T740 4 T760 4 T780 4 T800 4 T820 4 T840 4 T860 4 T880 4 T900 4 T920 4 T940 4 T960 4 T980 4 T1000 4 T1020 4 T1040 4 T1060 4 T1080 4 T1100 4 T1120 4 T1140 4 T1160 4 T1180 4 T1200 4" fill="none" stroke="var(--wave)" stroke-width="3"/>
</svg>

<!-- doctor -->
<section class="abs doctor"></section>
<div class="photo" style="left:93px;top:761px;width:314px;height:346px;background:linear-gradient(135deg,#e9e4df,#f1d8c6 50%,#f7f3ef)" role="img" aria-label="Photo of hands massaging a patient's foot"></div>
<h2 class="abs heading" style="left:434px;top:777px;font-size:26px">Meet<br>Dr Halvik</h2>
<p class="abs copy" style="left:438px;top:848px;width:310px">Sed in dui in augue consectetur lobortis. Pellentesque orci tellus, imperdiet interdum nibh a, varius gravida augue. Curabitur faucibus, lectus vitae maximus scelerisque, nunc arcu molestie erat, congue efficitur ante enim eget mi. Phasellus id felis laoreet, viverra purus eget, hendrerit nulla. Aenean interdum mollis gravida. Sed consectetur sit amet sapien vel iaculis. Phasellus iaculis dapibus ligula, non condimentum dolor semper sit amet.</p>
<a class="btn" style="left:576px;top:1175px">read more</a>
<h3 class="abs heading" style="left:99px;top:1129px;font-size:20px">Technique and care</h3>
<p class="abs copy" style="left:99px;top:1154px;width:300px">Sed in dui in augue consectetur lobortis. Pellentesque orci tellus, imperdiet interdum nibh a, varius</p>
<div class="photo" style="left:772px;top:774px;width:314px;height:238px;background:linear-gradient(160deg,#4a5660,#7b7a70 45%,#b89b80 75%,#8d8f84)" role="img" aria-label="Photo of a runner holding a bandaged knee"></div>
<h2 class="abs heading" style="left:773px;top:1026px;font-size:26px;line-height:1.45">Don’t get used<br>to feeling pain</h2>
<p class="abs copy" style="left:778px;top:1094px;width:320px">Lorem ipsum dolor sit amet, consectetur adipiscing elit. Praesent hendrerit quis enim ac vehicula. Sed in dui in augue consectetur lobortis. Pellentesque orci tellus, imperdiet</p>

<svg class="wave" style="top:1272px" viewBox="0 0 1200 8" preserveAspectRatio="none" aria-hidden="true">
  <path d="M0 4 Q10 0 20 4 T40 4 T60 4 T80 4 T100 4 T120 4 T140 4 T160 4 T180 4 T200 4 T220 4 T240 4 T260 4 T280 4 T300 4 T320 4 T340 4 T360 4 T380 4 T400 4 T420 4 T440 4 T460 4 T480 4 T500 4 T520 4 T540 4 T560 4 T580 4 T600 4 T620 4 T640 4 T660 4 T680 4 T700 4 T720 4 T740 4 T760 4 T780 4 T800 4 T820 4 T840 4 T860 4 T880 4 T900 4 T920 4 T940 4 T960 4 T980 4 T1000 4 T1020 4 T1040 4 T1060 4 T1080 4 T1100 4 T1120 4 T1140 4 T1160 4 T1180 4 T1200 4" fill="none" stroke="var(--wave)" stroke-width="3"/>
</svg>

<!-- welcome -->
<section class="abs welcome" role="img" aria-label="Faded photo of a therapist's hands holding a patient's hand"></section>
<h3 class="abs label" style="left:151px;top:1336px">Be Welcome</h3>
<p class="abs" style="left:170px;top:1374px;width:404px;font-size:16px;line-height:1.5">Donec pretium mattis augue vel bibendum. Mauris non nibh in tortor placerat pharetra. Nunc ut lacinia elit. Mauris nec ante ac quam dictum suscipit. Sed orci quam, fringilla vitae semper at, venenatis vel tellus. Suspendisse lacinia laoreet turpis et blandit. Pellentesque habitant morbi tristique senectus et netus et malesuada fames ac turpis egestas.</p>
<h3 class="abs label" style="left:660px;top:1336px">About us</h3>
<p class="abs" style="left:680px;top:1374px;width:404px;font-size:16px;line-height:1.5">Donec pretium mattis augue vel bibendum. Mauris non nibh in tortor placerat pharetra. Nunc ut lacinia elit. Mauris nec ante ac quam dictum suscipit. Sed orci quam, fringilla vitae semper at, venenatis vel tellus. Suspendisse lacinia laoreet turpis et blandit. Pellentesque habitant morbi tristique senectus et netus et malesuada fames ac turpis egestas.</p>
<a class="btn" style="left:914px;top:1565px">read more</a>

<svg class="wave" style="top:1767px" viewBox="0 0 1200 8" preserveAspectRatio="none" aria-hidden="true">
  <path d="M0 4 Q10 0 20 4 T40 4 T60 4 T80 4 T100 4 T120 4 T140 4 T160 4 T180 4 T200 4 T220 4 T240 4 T260 4 T280 4 T300 4 T320 4 T340 4 T360 4 T380 4 T400 4 T420 4 T440 4 T460 4 T480 4 T500 4 T520 4 T540 4 T560 4 T580 4 T600 4 T620 4 T640 4 T660 4 T680 4 T700 4 T720 4 T740 4 T760 4 T780 4 T800 4 T820 4 T840 4 T860 4 T880 4 T900 4 T920 4 T940 4 T960 4 T980 4 T1000 4 T1020 4 T1040 4 T1060 4 T1080 4 T1100 4 T1120 4 T1140 4 T1160 4 T1180 4 T1200 4" fill="none" stroke="var(--wave)" stroke-width="3"/>
</svg>

<!-- methodology -->
<section class="abs method"></section>
<h2 class="abs heading" style="left:94px;top:1826px;font-size:36px">Our methodology</h2>
<p class="abs" style="left:94px;top:1866px;width:480px;font-size:16px;line-height:1.45">Quisque tincidunt quam a porta sagittis. Etiam at urna dolor. Curabitur semper, arcu ut consequat sagittis, arcu purus venenatis est, et tristique nibh nibh porttitor odio. Nunc blandit ac ante in accumsan. Vestibulum ac tincidunt eros. Suspendisse elementum in nisi ut fringilla. Suspendisse tincidunt orci sit amet tellus porta placerat. Nunc sed turpis ullamcorper, cursus sapien a, placerat massa. Duis auctor eleifend est, et maximus est sagittis vel. In sit amet nisi tempus, pulvinar ipsum vel, scelerisque felis. Aliquam</p>
<a class="btn" style="left:402px;top:2095px">read more</a>
<div class="photo" style="left:604px;top:1818px;width:317px;height:202px;background:linear-gradient(180deg,#e4e6e2 0%,#c9c7c0 30%,#8b6a62 60%,#5a4440 100%)" role="img" aria-label="Photo of a relaxed back with a line of flowers laid across it"></div>
<h2 class="abs heading" style="left:604px;top:2040px;font-size:33px">Health for a peaceful life</h2>
<p class="abs" style="left:605px;top:2078px;width:475px;font-size:16px;line-height:1.4">Quisque tincidunt quam a porta sagittis. Etiam at urna dolor. Curabitur semper, arcu ut consequat sagittis, arcu purus venenatis est, et tristique nibh nibh porttitor odio. Nunc blandit ac ante in</p>
<p class="abs heading" style="left:604px;top:2142px;font-size:21px;font-weight:600">eternatitem magistima chose</p>

<!-- footer -->
<footer class="abs footer"></footer>
<div class="foot-col" style="left:98px">
  <h3>ABOUT</h3>
  <p>Quisque fermentum non turpis at porttitor. Nulla interdum erat sed dui maximus, sit amet lacinia libero posuere. Cras bibendum maximus justo vitae rhoncus. Etiam non vulputate nulla. Aliquam vehicula velit vitae</p>
</div>
<div class="foot-col" style="left:352px">
  <h3>RESOURCES</h3>
  <ul><li>SERVICES</li><li>CONTACT</li><li>ABOUT US</li><li>TESTIMONIAL</li><li>PORTFOLIO</li><li>SPECIALITIES</li></ul>
</div>
<div class="foot-col" style="left:608px">
  <h3>WHERE TO FIND US</h3>
  <p style="line-height:1.7">Street Lorem ipsum<br>Avenue dolor sit amet<br>Quod magis existerat, 27.<br>481291-291</p>
</div>
<div class="foot-col" style="left:862px">
  <h3>LOREM IPSUM</h3>
  <p>Quisque fermentum non turpis at porttitor. Nulla interdum erat sed dui maximus</p>
  <p style="margin-top:22px">Cras bibendum maximus justo vitae rhoncus. Etiam non vulputate nulla.</p>
</div>

</body>
</html>
```